Loom Haven needs a website

I sell rugs and carpet on my website, loomhavenfloors.example. I need help with the site design to make it "pop". The logo in the header has been designed and I want the site to match it's style and color. Also I have some example sites for layout:
matvale.example
weave-outlet.example

Industry/Entity Type

Carpet

Requirements
Must have
• Scrolling images on front page. I will insert photos, just need the code.

```html
<!DOCTYPE html>
<html lang="en">
<head>
<meta charset="utf-8">
<title>Loom Haven — Rugs and Carpets</title>
<link href="https://fonts.googleapis.com/css2?family=Quicksand:wght@400;500;700&family=Open+Sans:wght@400;600;700&display=swap" rel="stylesheet">
<style>
:root{
  --navy:#1d4272;
  --navy-dark:#173659;
  --ink:#111111;
  --text:#333333;
  --muted:#777777;
  --paper:#ffffff;
  --footer:#f4f4f4;
  --line:#d9d9d9;
}
*{margin:0;padding:0;box-sizing:border-box}
html,body{width:1200px;height:2205px;overflow:hidden;background:var(--paper)}
body{position:relative;font-family:"Open Sans",Arial,sans-serif;color:var(--text)}
.abs{position:absolute}
a{color:inherit;text-decoration:none}

/* top bar */
.topbar{left:0;top:0;width:1200px;height:37px;background:var(--ink);color:#bbb;font-size:11px}
.topbar .links{position:absolute;left:173px;top:11px;display:flex;gap:30px}
.topbar .locale{position:absolute;right:170px;top:11px;display:flex;gap:16px}

/* header */
.brand{left:171px;top:78px;display:flex;align-items:center;gap:14px}
.brand .mark{width:58px;height:58px;background:var(--ink)}
.brand .name{font-family:"Quicksand",sans-serif;font-weight:700;font-size:36px;color:var(--navy);letter-spacing:1px}
.search{left:551px;top:108px;width:236px;height:45px;border:1px solid var(--line);font-size:11px;color:#aaa;letter-spacing:1px;padding:15px 14px}
.search svg{position:absolute;right:10px;top:11px}
.cart{left:794px;top:108px;width:235px;height:45px;background:var(--ink);color:#fff;font-size:11px;font-weight:700;letter-spacing:1px}
.cart .icon{position:absolute;left:0;top:0;width:45px;height:45px;background:var(--navy);display:flex;align-items:center;justify-content:center}
.cart .label{position:absolute;left:72px;top:15px}

/* nav */
.nav{left:171px;top:208px;width:858px;height:71px;background:var(--navy);display:flex}
.nav a{flex:1;display:flex;align-items:center;justify-content:center;color:#fff;font-family:"Quicksand",sans-serif;font-weight:700;font-size:15px;letter-spacing:1px;border-right:1px solid rgba(255,255,255,.14)}
.nav a:last-child{border-right:none}

/* hero */
.hero{left:0;top:279px;width:1200px;height:460px;background:linear-gradient(180deg,#5b4c3c 0%,#8a7458 45%,#5a4636 75%,#3b3129 100%)}
.hero h1{position:absolute;left:0;right:0;top:78px;text-align:center;color:#fff;font-family:"Quicksand",sans-serif;font-weight:700;font-size:33px;letter-spacing:2px}
.hero .tag{position:absolute;left:0;right:0;top:302px;text-align:center;color:#fff;font-family:"Quicksand",sans-serif;font-weight:700;font-size:26px}
.arrow{width:76px;height:76px;border:2px solid rgba(255,255,255,.85);border-radius:50%;top:192px}

/* category tiles */
.tile{top:682px;width:424px;height:283px}
.tile .photo{position:absolute;left:0;top:0;width:424px;height:200px}
.tile .bar{position:absolute;left:0;top:200px;width:424px;height:83px;background:var(--navy);color:#fff;padding:12px 0 0 14px}
.tile .kicker{font-family:"Quicksand",sans-serif;font-size:15px;letter-spacing:1px}
.tile .title{font-family:"Quicksand",sans-serif;font-weight:700;font-size:38px;letter-spacing:3px;line-height:44px}
.tile .go{position:absolute;right:0;top:200px;width:71px;height:83px;background:var(--ink);display:flex;align-items:center;justify-content:center}

/* banner */
.banner{left:171px;top:998px;width:858px;height:255px;background:linear-gradient(135deg,#cfcdc8 0%,#a9a6a0 50%,#7c7a75 100%);text-align:center;color:#fff}
.banner .kicker{position:absolute;left:0;right:0;top:28px;font-family:"Quicksand",sans-serif;font-size:37px;letter-spacing:4px}
.banner .title{position:absolute;left:0;right:0;top:76px;font-family:"Quicksand",sans-serif;font-weight:700;font-size:58px;letter-spacing:3px}
.banner .shop{position:absolute;left:307px;top:154px;width:246px;height:68px;border:2px solid #fff;font-family:"Quicksand",sans-serif;font-weight:700;font-size:22px;letter-spacing:2px;line-height:64px}

/* features */
.feature{top:1283px;display:flex;align-items:center;gap:14px}
.feature .ring{width:140px;height:140px;border:4px solid var(--ink);border-radius:50%;display:flex;align-items:center;justify-content:center}
.feature .lead{font-family:"Quicksand",sans-serif;font-size:23px;letter-spacing:1px;color:var(--ink);line-height:27px}
.feature .strong{font-family:"Quicksand",sans-serif;font-weight:700;font-size:23px;letter-spacing:2px;color:var(--navy);line-height:27px}

/* latest */
.latest{left:171px;top:1450px;width:858px;height:72px;background:var(--navy)}
.latest h2{position:absolute;left:20px;top:20px;color:#fff;font-family:"Quicksand",sans-serif;font-size:27px;font-weight:400;letter-spacing:2px}
.latest h2 b{font-weight:700}
.latest .more{position:absolute;right:0;top:0;width:189px;height:72px;background:var(--ink);color:#fff;font-size:14px;font-weight:600;letter-spacing:1px;display:flex;align-items:center;justify-content:center}

.product{top:1545px;width:195px}
.product .photo{width:195px;height:159px}
.product .kicker{margin-top:20px;font-family:"Quicksand",sans-serif;font-size:17px;letter-spacing:1px;color:#444}
.product .title{font-family:"Quicksand",sans-serif;font-weight:700;font-size:34px;letter-spacing:2px;color:var(--navy);line-height:38px}
.product .desc{font-size:12px;line-height:17px;color:#333;margin-top:3px}
.product .price{font-size:16px;font-weight:700;color:var(--ink);margin-top:5px;letter-spacing:1px}
.product .actions{display:flex;gap:4px;margin-top:8px}
.product .add{width:66px;height:48px;background:var(--ink);display:flex;align-items:center;justify-content:center}
.product .details{width:101px;height:48px;background:var(--navy);color:#fff;font-size:13px;font-weight:600;letter-spacing:1px;display:flex;align-items:center;justify-content:center}

/* footer */
.footer{left:0;top:1935px;width:1200px;height:212px;background:var(--footer)}
.col{top:1980px}
.col h3{font-family:"Quicksand",sans-serif;font-weight:700;font-size:15px;letter-spacing:2px;color:var(--navy);margin-bottom:14px}
.col li{list-style:none;font-size:10px;color:#222;line-height:20px;text-transform:uppercase}
.social{display:flex;gap:14px}
.social span{width:12px;height:12px;border-radius:50%;background:var(--ink)}
.newsletter input{display:block;width:160px;height:33px;border:1px solid var(--line);background:#fff;font-size:10px;padding:0 10px;color:#999;font-family:inherit}
.newsletter .subscribe{margin-top:5px;width:160px;height:33px;background:var(--ink);color:#fff;font-size:11px;font-weight:700;letter-spacing:1px;display:flex;align-items:center;justify-content:center}
.bottombar{left:0;top:2147px;width:1200px;height:58px;background:var(--ink);color:#fff;font-size:11px;text-align:center;line-height:58px;font-weight:600}
</style>
</head>
<body>

<div class="abs topbar">
  <div class="links"><a>Home</a><a>Login</a><a>Register</a><a>Sign Up</a><a>My Account</a><a>Checkout</a></div>
  <div class="locale"><span>EN ▾</span><span>$ ▾</span></div>
</div>

<div class="abs brand"><span class="mark"></span><span class="name">loom haven</span></div>

<div class="abs search">SEARCH
  <svg width="22" height="22" viewBox="0 0 22 22" fill="none" stroke="#bbb" stroke-width="2"><circle cx="9" cy="9" r="7"/><line x1="14" y1="14" x2="20" y2="20"/></svg>
</div>

<div class="abs cart">
  <div class="icon"><svg width="22" height="20" viewBox="0 0 22 20" fill="none" stroke="#fff" stroke-width="2"><path d="M1 2h4l3 11h11l2-8H7"/><circle cx="9" cy="17" r="1.5"/><circle cx="18" cy="17" r="1.5"/></svg></div>
  <div class="label">SHOPPING CART - (0)</div>
</div>

<nav class="abs nav"><a>HOME</a><a>ABOUT</a><a>RUGS</a><a>CARPETS</a><a>HARDWOOD</a><a>CONTACT</a></nav>

<section class="abs hero" role="img" aria-label="Slideshow photo of a modern bedroom with a white bed on a grey shag rug and wood floor">
  <h1>SELLING BEST RUGS AND CARPETS !</h1>
  <div class="tag">Loom Haven</div>
  <div class="abs arrow" style="left:47px"><svg width="72" height="72" viewBox="0 0 72 72" fill="none" stroke="#fff" stroke-width="2"><polyline points="41,24 29,36 41,48"/></svg></div>
  <div class="abs arrow" style="left:1076px"><svg width="72" height="72" viewBox="0 0 72 72" fill="none" stroke="#fff" stroke-width="2"><polyline points="31,24 43,36 31,48"/></svg></div>
</section>

<div class="abs tile" style="left:171px">
  <div class="photo" role="img" aria-label="Photo of a white shag rug on a wooden floor" style="background:linear-gradient(135deg,#c9a56b 0%,#f3ece0 40%,#efe6d6 70%,#b98d55 100%)"></div>
  <div class="bar"><div class="kicker">LOOM HAVEN</div><div class="title">RUGS</div></div>
  <div class="go"><svg width="20" height="34" viewBox="0 0 20 34" fill="none" stroke="#fff" stroke-width="2"><polyline points="3,3 17,17 3,31"/></svg></div>
</div>
<div class="abs tile" style="left:605px">
  <div class="photo" role="img" aria-label="Photo of a living room with white sofas and a city view" style="background:linear-gradient(160deg,#b8c3cc 0%,#8d8a83 45%,#4a3d33 100%)"></div>
  <div class="bar"><div class="kicker">LOOM HAVEN</div><div class="title">CARPETS</div></div>
  <div class="go"><svg width="20" height="34" viewBox="0 0 20 34" fill="none" stroke="#fff" stroke-width="2"><polyline points="3,3 17,17 3,31"/></svg></div>
</div>

<section class="abs banner" role="img" aria-label="Photo of a bright room with an orange sofa and a striped rug">
  <div class="kicker">LOOM HAVEN</div>
  <div class="title">RUGS AND CARPETS</div>
  <div class="shop">SHOP NOW</div>
</section>

<div class="abs feature" style="left:173px">
  <div class="ring"><svg width="70" height="50" viewBox="0 0 70 50"><rect x="2" y="8" width="40" height="28" fill="#111"/><path d="M44 16h14l9 10v10H44z" fill="#111"/><circle cx="14" cy="40" r="6" fill="#111" stroke="#fff" stroke-width="2"/><circle cx="56" cy="40" r="6" fill="#111" stroke="#fff" stroke-width="2"/><text x="22" y="27" font-family="Open Sans, sans-serif" font-size="11" font-weight="700" fill="#fff" text-anchor="middle">FREE</text></svg></div>
  <div><div class="lead">Free</div><div class="strong">SHIPPING</div></div>
</div>
<div class="abs feature" style="left:488px">
  <div class="ring"><svg width="64" height="58" viewBox="0 0 64 58" fill="none" stroke="#111" stroke-width="4"><path d="M2 10h10l8 30h32l8-22H16"/><circle cx="24" cy="50" r="4" fill="#111"/><circle cx="48" cy="50" r="4" fill="#111"/><path d="M38 4c6 6 2 10 0 14" stroke-width="3"/></svg></div>
  <div><div class="lead">ORDER</div><div class="strong">ONLINE</div></div>
</div>
<div class="abs feature" style="left:781px">
  <div class="ring"><svg width="60" height="60" viewBox="0 0 60 60" fill="none" stroke="#111" stroke-width="3.5"><path d="M6 22l24-10 24 10v26L30 58 6 48z"/><path d="M6 22l24 10 24-10M30 32v26"/><path d="M30 2v16M23 11l7 7 7-7" stroke="#1d4272"/></svg></div>
  <div><div class="lead">SPECIAL</div><div class="strong">OFFER</div></div>
</div>

<div class="abs latest">
  <h2>LATEST <b>PRODUCTS</b></h2>
  <div class="more">MORE PRODUCTS</div>
</div>

<div class="abs product" style="left:171px">
  <div class="photo" role="img" aria-label="Photo of a white living room with shelves and a light rug" style="background:linear-gradient(160deg,#f2f2f0 0%,#d9dcdc 60%,#b7b9b6 100%)"></div>
  <div class="kicker">LOOM HAVEN</div><div class="title">RUGS</div>
  <div class="desc">Lorem ipsum dolor sit amet, the consectetuer adipiscing elit,</div>
  <div class="price">$ 23.89</div>
  <div class="actions"><div class="add"><svg width="20" height="18" viewBox="0 0 22 20" fill="none" stroke="#fff" stroke-width="2"><path d="M1 2h4l3 11h11l2-8H7"/><circle cx="9" cy="17" r="1.5"/><circle cx="18" cy="17" r="1.5"/></svg></div><div class="details">DETAILS</div></div>
</div>
<div class="abs product" style="left:391px">
  <div class="photo" role="img" aria-label="Photo of a red shag carpet in a white room" style="background:linear-gradient(180deg,#ecebe8 0%,#e4e0dc 42%,#c3182a 55%,#9c0f1e 100%)"></div>
  <div class="kicker">LOOM HAVEN</div><div class="title">CARPETS</div>
  <div class="desc">Lorem ipsum dolor sit amet, the consectetuer adipiscing elit,</div>
  <div class="price">$ 23.89</div>
  <div class="actions"><div class="add"><svg width="20" height="18" viewBox="0 0 22 20" fill="none" stroke="#fff" stroke-width="2"><path d="M1 2h4l3 11h11l2-8H7"/><circle cx="9" cy="17" r="1.5"/><circle cx="18" cy="17" r="1.5"/></svg></div><div class="details">DETAILS</div></div>
</div>
<div class="abs product" style="left:612px">
  <div class="photo" role="img" aria-label="Photo of a lounge with white sofas and a wooden coffee table" style="background:linear-gradient(160deg,#8a7a66 0%,#c9bba6 45%,#6a5240 100%)"></div>
  <div class="kicker">LOOM HAVEN</div><div class="title">RUGS</div>
  <div class="desc">Lorem ipsum dolor sit amet, the consectetuer adipiscing elit,</div>
  <div class="price">$ 23.89</div>
  <div class="actions"><div class="add"><svg width="20" height="18" viewBox="0 0 22 20" fill="none" stroke="#fff" stroke-width="2"><path d="M1 2h4l3 11h11l2-8H7"/><circle cx="9" cy="17" r="1.5"/><circle cx="18" cy="17" r="1.5"/></svg></div><div class="details">DETAILS</div></div>
</div>
<div class="abs product" style="left:834px">
  <div class="photo" role="img" aria-label="Photo of a grey living room with a wall unit and a pale carpet" style="background:linear-gradient(170deg,#8f8a8a 0%,#b8b1ad 50%,#d8d2cc 100%)"></div>
  <div class="kicker">LOOM HAVEN</div><div class="title">CARPETS</div>
  <div class="desc">Lorem ipsum dolor sit amet, the consectetuer adipiscing elit,</div>
  <div class="price">$ 23.89</div>
  <div class="actions"><div class="add"><svg width="20" height="18" viewBox="0 0 22 20" fill="none" stroke="#fff" stroke-width="2"><path d="M1 2h4l3 11h11l2-8H7"/><circle cx="9" cy="17" r="1.5"/><circle cx="18" cy="17" r="1.5"/></svg></div><div class="details">DETAILS</div></div>
</div>

<footer class="abs footer"></footer>
<div class="abs col" style="left:171px"><h3>MENU</h3><ul><li>Home</li><li>About</li><li>Rugs</li><li>Carpets</li><li>Contact</li></ul></div>
<div class="abs col" style="left:309px"><h3>MY ACCOUNT</h3><ul><li>Login</li><li>Register</li><li>Sign Up</li><li>Checkout</li></ul></div>
<div class="abs col" style="left:509px"><h3>INFORMATION</h3><ul><li>Privacy Policy</li><li>Sitemap</li><li>Terms &amp; Condition</li></ul></div>
<div class="abs col" style="left:713px"><h3>SOCIAL</h3><div class="social"><span></span><span></span><span></span></div></div>
<div class="abs col newsletter" style="left:867px"><h3>NEWSLETTER</h3><input type="text" value="E-MAIL" aria-label="E-mail"><div class="subscribe">SUBSCRIBE</div></div>

<div class="abs bottombar">Copyrights © 2014 Loom Haven, LLC</div>

</body>
</html>
```